Fiber to the home

This postcard campaign is to announce the availability of our fiber optic high speed Internet service in select neighborhoods. I have attached our company logo. Look forward to seeing what you come up with.

Industry/Entity Type

Internet

```html
<!DOCTYPE html>
<html lang="en">
<head>
<meta charset="utf-8">
<title>Lumacore Fiber Postcard</title>
<link rel="stylesheet" href="https://fonts.googleapis.com/css2?family=Roboto+Condensed:wght@400;700;800&family=Montserrat:wght@400;500;600;700&display=swap">
<style>
:root{
  --backdrop:#a19fa0;
  --paper:#ffffff;
  --navy:#1c1f5e;
  --navy-deep:#16184a;
  --sky:#1aa3e6;
  --royal:#1450a8;
  --royal-light:#0c72d0;
  --ink:#111111;
  --grey-zone:#efefef;
  --grey-label:#b8b8b8;
  --photo-a:#c9b8a4;
  --photo-b:#8a93a3;
}
*{margin:0;padding:0;box-sizing:border-box}
html,body{width:806px;height:1200px;overflow:hidden}
body{background:var(--backdrop);position:relative;font-family:"Montserrat",sans-serif;color:var(--ink)}
.card{position:absolute;width:641px;height:492px;background:var(--paper);overflow:hidden;box-shadow:3px 4px 8px rgba(0,0,0,.35)}
.card--front{left:80px;top:70px}
.card--back{left:81px;top:633px}
.abs{position:absolute;white-space:nowrap}
.cond{font-family:"Roboto Condensed",sans-serif}

/* front */
.hero-photo{left:0;top:0;width:641px;height:300px;background:linear-gradient(135deg,#e9e4dc 0%,var(--photo-a) 40%,var(--photo-b) 100%)}
.front-shapes{left:0;top:0}
.brand{display:flex;align-items:center;gap:7px;font-family:"Roboto Condensed",sans-serif;font-weight:800;font-size:26px;color:var(--ink);letter-spacing:.3px}
.brand-dot{width:13px;height:13px;border-radius:50%;background:var(--ink)}
.front-brand{left:18px;top:26px}
.headline-top{left:26px;top:302px;font-size:30px;font-weight:800;color:var(--navy);letter-spacing:.3px}
.headline-main{left:26px;top:340px;font-size:42px;font-weight:700;color:var(--sky)}
.headline-sub{left:27px;top:398px;font-size:19px;font-weight:700;color:var(--ink);letter-spacing:.5px}
.call-bar{background:var(--navy-deep);color:#fff;display:flex;align-items:center}
.call-bar__label{font-weight:400;letter-spacing:.5px}
.call-bar__rule{width:1px;background:rgba(255,255,255,.55);align-self:stretch;margin:8px 8px}
.call-bar__number{font-weight:700}
.front-call{left:0;top:437px;width:383px;height:55px;padding-left:26px}
.front-call .call-bar__label{font-size:23px}
.front-call .call-bar__number{font-size:29px}
.plans{left:385px;top:222px;width:256px;height:270px;color:#fff}
.plans__title{position:absolute;left:0;width:256px;top:46px;text-align:center;font-family:"Roboto Condensed",sans-serif;font-weight:700;font-size:20px;letter-spacing:.4px}
.plan{position:absolute;left:8px;width:240px;height:50px;display:flex;align-items:center}
.plan__bullet{width:11px;height:11px;margin-right:9px;align-self:flex-start;margin-top:8px}
.plan__text{flex:1;font-size:14px;line-height:20px;font-weight:500}
.plan__rule{width:1px;height:40px;background:rgba(255,255,255,.45);margin-right:14px}
.plan__price{font-size:18px;font-weight:700;width:48px}
.plans__rule{position:absolute;left:8px;width:236px;top:222px;height:1px;background:rgba(255,255,255,.6)}
.plans__more{position:absolute;left:0;width:256px;top:230px;text-align:center;font-size:12.5px;font-weight:700;letter-spacing:.2px;line-height:15px}
.plans__url{position:absolute;left:0;width:256px;top:246px;text-align:center;font-size:13px;font-weight:600;line-height:16px}

/* back */
.mail-zone{left:0;top:0}
.mail-label{color:var(--grey-label);font-size:17px;text-align:center}
.back-title{left:24px;top:24px;font-size:27px;font-weight:700;color:var(--sky);letter-spacing:.2px}
.back-sub{left:22px;top:64px;font-size:16px;font-weight:700;color:var(--navy);letter-spacing:.5px}
.back-brand{left:316px;top:38px}
.options-tab{left:0;top:103px;width:190px;height:37px;background:linear-gradient(90deg,var(--royal),var(--royal-light));color:#fff;font-family:"Roboto Condensed",sans-serif;font-weight:700;font-size:18px;line-height:37px;padding-left:22px}
.option{left:18px;color:var(--ink)}
.option__bullet{position:absolute;left:0;top:4px;width:12px;height:12px}
.option__body{margin-left:24px}
.option__name{font-size:15px;font-weight:700;color:var(--navy)}
.option__small{font-size:10px;line-height:13px}
.option__line{font-size:13.5px;line-height:15px}
.option-rule{left:184px;width:1px;background:#c8c8c8}
.option-price{left:212px;font-size:21px;font-weight:700;color:var(--navy)}
.back-call{left:0;top:303px;width:301px;height:45px;padding-left:20px}
.back-call .call-bar__label{font-size:20px}
.back-call .call-bar__number{font-size:23px}
.back-more{left:0;width:301px;top:358px;text-align:center;font-size:12.5px;font-weight:700}
.back-url{left:0;width:301px;top:373px;text-align:center;font-size:17px;font-weight:500}
.back-note{left:18px;top:402px;font-family:"Roboto Condensed",sans-serif;font-size:11px;font-weight:700;color:var(--navy)}
</style>
</head>
<body>

<section class="card card--front">
  <div class="abs hero-photo" role="img" aria-label="Photo of a smiling family of four gathered on a sofa using a phone, tablet and laptop"></div>
  <svg class="abs front-shapes" width="641" height="492" viewBox="0 0 641 492">
    <defs>
      <linearGradient id="planGrad" x1="0" y1="0" x2="1" y2="1">
        <stop offset="0" stop-color="#1d58b4"/>
        <stop offset="1" stop-color="#0a6fd0"/>
      </linearGradient>
    </defs>
    <polygon points="0,240 385,284 385,292 0,250" fill="#1aa3e6"/>
    <polygon points="0,250 385,292 385,492 0,492" fill="#ffffff"/>
    <polygon points="385,262 641,224 641,492 385,492" fill="url(#planGrad)"/>
    <polygon points="560,236 641,214 641,224" fill="#1c1f5e"/>
  </svg>

  <div class="abs brand front-brand"><span class="brand-dot"></span>LUMACORE</div>

  <div class="abs headline-top cond">FIBER OPTIC HIGH SPEED</div>
  <div class="abs headline-main cond">INTERNET SERVICE</div>
  <div class="abs headline-sub">AFFORDABLE, FAST, RELIABLE</div>

  <div class="abs call-bar front-call">
    <span class="call-bar__label">CALL US</span><span class="call-bar__rule"></span><span class="call-bar__number">866-555-0142</span>
  </div>

  <div class="abs plans">
    <div class="plans__title">RESIDENTIAL PLANS</div>
    <div class="plan" style="top:66px">
      <svg class="plan__bullet" viewBox="0 0 12 12"><circle cx="6" cy="6" r="5" fill="none" stroke="#fff" stroke-width="1.4"/><path d="M1 6h10M6 1v10" stroke="#fff" stroke-width="1.2"/></svg>
      <div class="plan__text">20 Mbps<br>STANDARD FIBER</div><span class="plan__rule"></span><div class="plan__price">$35</div>
    </div>
    <div class="plan" style="top:116px">
      <svg class="plan__bullet" viewBox="0 0 12 12"><circle cx="6" cy="6" r="5" fill="none" stroke="#fff" stroke-width="1.4"/><path d="M1 6h10M6 1v10" stroke="#fff" stroke-width="1.2"/></svg>
      <div class="plan__text">30 Mbps<br>TURBO FIBER</div><span class="plan__rule"></span><div class="plan__price">$45</div>
    </div>
    <div class="plan" style="top:166px">
      <svg class="plan__bullet" viewBox="0 0 12 12"><circle cx="6" cy="6" r="5" fill="none" stroke="#fff" stroke-width="1.4"/><path d="M1 6h10M6 1v10" stroke="#fff" stroke-width="1.2"/></svg>
      <div class="plan__text">50 Mbps<br>EXTREME FIBER</div><span class="plan__rule"></span><div class="plan__price">$55</div>
    </div>
    <div class="plans__rule"></div>
    <div class="plans__more">FOR MORE INFORMATION</div>
    <div class="plans__url">www.lumacorenet.com</div>
  </div>
</section>

<section class="card card--back">
  <svg class="abs mail-zone" width="641" height="492" viewBox="0 0 641 492">
    <polygon points="493,0 641,0 641,492 85,492 85,424 338,424 338,162 493,162" fill="#efefef"/>
  </svg>
  <div class="abs mail-label" style="left:493px;top:62px;width:148px;line-height:20px">Postage<br>Area</div>
  <div class="abs mail-label" style="left:338px;top:285px;width:303px">Address Area</div>
  <div class="abs mail-label" style="left:85px;top:446px;width:500px">Barcode Area</div>

  <div class="abs back-title cond">BROADBAND INTERNET</div>
  <div class="abs back-sub">AFFORDABLE, FAST, RELIABLE</div>
  <div class="abs brand back-brand"><span class="brand-dot"></span>LUMACORE</div>

  <div class="abs options-tab">ADDITIONAL OPTIONS</div>

  <div class="abs option" style="top:155px">
    <svg class="option__bullet" viewBox="0 0 12 12"><circle cx="6" cy="6" r="5" fill="none" stroke="#1c1f5e" stroke-width="1.4"/><path d="M1 6h10M6 1v10" stroke="#1c1f5e" stroke-width="1.2"/></svg>
    <div class="option__body">
      <div class="option__name">Unlimited Phone</div>
      <div class="option__small">Keep same phone number</div>
      <div class="option__line">Includes voice mail<br>to e-mail</div>
    </div>
  </div>
  <div class="abs option-rule" style="top:150px;height:70px"></div>
  <div class="abs option-price" style="top:172px">$29</div>

  <div class="abs option" style="top:233px">
    <svg class="option__bullet" viewBox="0 0 12 12"><circle cx="6" cy="6" r="5" fill="none" stroke="#1c1f5e" stroke-width="1.4"/><path d="M1 6h10M6 1v10" stroke="#1c1f5e" stroke-width="1.2"/></svg>
    <div class="option__body">
      <div class="option__name">Wireless Internet</div>
      <div class="option__line">10 Mbps</div>
      <div class="option__line" style="margin-top:5px">BURST SPEED</div>
    </div>
  </div>
  <div class="abs option-rule" style="top:230px;height:58px"></div>
  <div class="abs option-price" style="top:250px">$29</div>

  <div class="abs call-bar back-call">
    <span class="call-bar__label">CALL US</span><span class="call-bar__rule"></span><span class="call-bar__number">866-555-0142</span>
  </div>
  <div class="abs back-more">FOR MORE INFORMATION</div>
  <div class="abs back-url">www.lumacorenet.com</div>
  <div class="abs back-note">Additional services available. All services not available in all areas.</div>
</section>

</body>
</html>
```